Consulting and solution company website in MS Webmatrix

We need a website for a new healthcare consulting company that provides management consulting and innovative solutions for patient safety. We offer 1 product with plans to add 2 more and we offer consulting services to implement, train, select, improve, the patient safety programs. We provide services to both patient safety organizations and health care provider's (mainly hospitals and health systems). We want the website to convey an innovative, hard-working, energetic company bringing new ideas to healthcare. We do not want a bunch of stock pictures of people looking smart and busy in suits and doctor/nurse garb. T We love adventure, jumping ino the middle of a problem, and are thrilled to be a small and disruptive startup. The problems are very serious and complex issues so we have to tasteful in the design but not typical and boring. he site must be in .net and be device responsive. We will manage the site in MS Webmatrix and if db is used it must be MS SQL. Many of the new and fresh templates I have seen are great. We just can't seem to pull it all together when we start "tweaking" the design. We have modified a standard template to demonstrate where we are headed, but need a higher quality than we are able to build.

My current test site is at http://sandbox.bravoridgeworks.example/

Sites I like
http://www.quillmerasoft.example/
http://fandor.velbrix.example/
https://www.taskharbor.example/
http://www.dealgrovehub.example/
http://www.wmrtq.example/

Companies in my market:
www.Kvboutcomes.example
www.Tundelcrew.example
www.Pxfixworks.example
www.Velimark.example

Target Market(s)

Healthcare providers like chief executives of hospitals, Nursing administrators, Patient Safety Professionals (www.gdwk.example) and physicians/Chief Medical Officers.

Industry/Entity Type

Management Consulting

Font styles to use
Sans Serif

Requirements
Must have
• Must have a put together feel graphically, clean, simple
Must be able to own all design materials.
Must be able to update content with some homework by us
Must have a picture slider
Must be based on .net/mssql.
Nice to have
• Blog page behind a registration process
Register and pull down whitepaper materials
Responsive design

```html
<!DOCTYPE html>
<html lang="en">
<head>
<meta charset="utf-8">
<title>CrestVane — Healthcare Consulting</title>
<link href="https://fonts.googleapis.com/css2?family=Oswald:wght@400;500&family=Open+Sans:ital,wght@0,400;0,600;0,700;1,700&display=swap" rel="stylesheet">
<style>
:root{
  --blue:#2b8fd8;
  --green:#2fc167;
  --green-text:#1fa34e;
  --red:#d2232a;
  --ink:#222;
  --text:#555;
  --muted:#8a8a8a;
  --card-bg:#f4f9fb;
  --card-line:#e1edf1;
  --dark:#2f2f2f;
  --bar:#ececec;
}
*{box-sizing:border-box;margin:0;padding:0}
html,body{width:1200px;height:2170px;overflow:hidden}
body{position:relative;background:#fff;font-family:"Open Sans",Arial,sans-serif;color:var(--text)}

/* header */
.site-header{position:absolute;top:0;left:0;width:1200px;height:80px;background:#fff}
.brand{position:absolute;left:161px;top:22px;display:flex;align-items:center;gap:8px;font-weight:700;font-size:24px;color:var(--ink)}
.brand-mark{width:14px;height:14px;background:var(--ink)}
.topline{position:absolute;right:162px;top:9px;font-size:12px;color:var(--ink);font-weight:700;display:flex;gap:22px}
.topline .mail{color:var(--blue);font-weight:400}
.topline .acct{color:var(--red)}
.main-nav{position:absolute;right:162px;top:46px;display:flex;gap:30px;font-size:13px;font-weight:600;color:var(--ink)}
.main-nav .active{color:var(--blue);border-bottom:2px solid var(--blue);padding-bottom:8px}

/* hero */
.hero{position:absolute;top:80px;left:0;width:1200px;height:556px;overflow:hidden;
  background:
    radial-gradient(ellipse 260px 230px at 930px 470px,#6e4a30 0%,#8a6344 45%,rgba(138,99,68,0) 100%),
    radial-gradient(ellipse 520px 170px at 330px 560px,#5d6670 0%,#8e979f 45%,rgba(142,151,159,0) 100%),
    radial-gradient(ellipse 500px 200px at 700px 160px,#ffffff 0%,rgba(255,255,255,0) 100%),
    linear-gradient(180deg,#b9c3cc 0%,#e6e9ec 30%,#f4f5f6 55%,#c6ccd1 80%,#9ea5ab 100%)}
.hero h1{position:absolute;left:161px;top:192px;font-family:"Oswald",sans-serif;font-weight:400;font-size:46px;line-height:54px;color:var(--ink)}
.hero h1 .accent{color:var(--green-text);display:block}
.hero .tagline{position:absolute;left:163px;top:305px;font-size:14px;font-weight:700;font-style:italic;color:var(--ink);text-transform:uppercase}
.hero .tagline em{color:var(--red)}
.btn-green{position:absolute;left:161px;top:360px;width:121px;height:35px;background:var(--green);color:#fff;font-size:15px;display:flex;align-items:center;justify-content:center}
.slider-dots{position:absolute;left:563px;top:532px;display:flex;gap:5px}
.slider-dots span{width:18px;height:4px;background:#fff}
.slider-dots .on{background:var(--green)}

/* intro cards */
.intro-card{position:absolute;top:690px;width:278px;height:330px;background:var(--card-bg);border:1px solid var(--card-line);text-align:center}
.intro-card svg{position:absolute;left:59px;top:18px}
.intro-card h3{position:absolute;top:176px;width:100%;font-size:15px;font-weight:600;color:var(--ink)}
.intro-card p{position:absolute;top:208px;left:22px;right:22px;font-size:11.5px;line-height:20px;color:var(--muted)}
.btn-outline{position:absolute;height:26px;width:98px;border:1px solid #bbb;font-size:12px;color:var(--muted);display:flex;align-items:center;justify-content:center}
.intro-card .btn-outline{left:89px;top:284px}

/* offer band */
.offer{position:absolute;top:1074px;left:0;width:1200px;height:439px;
  background:
    radial-gradient(ellipse 300px 160px at 560px 260px,rgba(70,62,54,.55) 0%,rgba(70,62,54,0) 100%),
    radial-gradient(ellipse at 50% 60%,#2c3531 0%,#161c1a 60%,#0d110f 100%)}
.section-title{display:flex;align-items:center;gap:9px;font-family:"Oswald",sans-serif;font-size:26px;font-weight:400}
.section-title .sq{width:11px;height:11px}
.offer .section-title{position:absolute;top:50px;left:0;width:1200px;justify-content:center;color:#fff}
.offer .section-title .sq{background:#fff}
.offer-item{position:absolute;top:144px;width:224px;text-align:center;color:#fff}
.offer-item svg{display:block;margin:0 auto}
.offer-item h3{margin-top:12px;font-size:15px;font-weight:600}
.offer-item p{margin-top:10px;font-size:12px;line-height:21px;color:#e8e8e8}
.offer-item .btn-outline{position:relative;margin:14px auto 0;border-color:#aaa;color:#ddd}

/* lower columns */
.lower .section-title{position:absolute;top:1562px;color:var(--ink);font-size:24px}
.lower .section-title .sq{background:var(--ink)}
.photo{position:absolute;top:1608px;width:278px;height:150px}
.photo.lab{background:
    radial-gradient(ellipse 70px 80px at 70px 110px,#f3f1ee 0%,rgba(243,241,238,0) 100%),
    radial-gradient(ellipse 80px 80px at 220px 115px,#efece8 0%,rgba(239,236,232,0) 100%),
    linear-gradient(180deg,#4e3b2c 0%,#7a5f47 30%,#b8a68f 55%,#e4ded6 100%)}
.photo.hands{background:
    radial-gradient(ellipse 120px 50px at 150px 90px,#e2b79b 0%,#d39d80 50%,rgba(211,157,128,0) 100%),
    linear-gradient(120deg,#2f86c9 0%,#79b8e2 35%,#cfe3f1 60%,#d9b39c 80%,#b98066 100%)}
.story h4,.news h4{position:absolute;font-size:14px;font-weight:600;color:var(--ink)}
.story p,.news p{position:absolute;width:278px;font-size:12px;line-height:20px;color:var(--muted)}
.news .date{position:absolute;font-size:11px;color:var(--muted)}
.news .more{color:var(--blue)}
.field{position:absolute;left:755px;width:278px;border:1px solid #d6d6d6;font-size:12px;color:var(--muted);padding:9px 10px}
.btn-dark{position:absolute;left:755px;top:1827px;width:130px;height:32px;background:var(--dark);color:#fff;font-size:12px;font-weight:700;display:flex;align-items:center;justify-content:center}

/* footer */
.site-footer{position:absolute;top:1910px;left:0;width:1200px;height:228px;background:var(--dark);color:#ddd}
.site-footer .brand{top:40px;color:#fff}
.site-footer .brand-mark{background:#fff}
.site-footer h5{position:absolute;top:40px;font-size:15px;font-weight:600;color:#fff}
.f-address{position:absolute;left:161px;top:75px;font-size:12px;line-height:20px}
.f-address b{color:#fff}
.f-address .link{color:#6fb5ea}
.f-links{position:absolute;left:423px;top:78px;font-size:12px;line-height:19.5px;list-style:none}
.f-input{position:absolute;left:612px;width:204px;height:29px;background:#fff;font-size:11px;color:#999;padding:7px 8px}
.f-btn{position:absolute;left:612px;top:154px;width:117px;height:27px;background:#6d6d6d;color:#fff;font-size:11px;font-weight:600;display:flex;align-items:center;justify-content:center}
.social{position:absolute;left:924px;top:76px;display:flex;gap:9px}
.social span{width:24px;height:24px;background:#e6e6e6}
.bottom-bar{position:absolute;top:2138px;left:0;width:1200px;height:32px;background:var(--bar);font-size:11px;color:#777}
.bottom-bar .copy{position:absolute;left:161px;top:9px}
.bottom-bar .legal{position:absolute;right:162px;top:9px;color:#555}
</style>
</head>
<body>

<header class="site-header">
  <div class="brand"><span class="brand-mark"></span>CrestVane</div>
  <div class="topline">
    <span>Call: 555.014.2297</span>
    <span>Email: <span class="mail">info@crestvanesolutions.example</span></span>
    <span class="acct">Register &nbsp;|&nbsp; Login</span>
  </div>
  <nav class="main-nav">
    <span class="active">Home</span><span>About</span><span>Services</span><span>Solutions</span><span>Contact</span>
  </nav>
</header>

<section class="hero" role="img" aria-label="Slider photo: two climbers on a rocky summit above the clouds, one pulling the other up">
  <h1>We Offer<span class="accent">Healthcare Consulting Services</span></h1>
  <p class="tagline">To implement, train, select, improve, the <em>patient safety programs.</em></p>
  <a class="btn-green">View More</a>
  <div class="slider-dots"><span class="on"></span><span></span><span></span></div>
</section>

<div class="intro-card" style="left:161px">
  <svg width="160" height="140" viewBox="0 0 160 140">
    <path d="M80 14 A62 62 0 1 0 142 76" fill="none" stroke="#dde3e6" stroke-width="5"/>
    <path d="M134 70 l8 10 l8 -10" fill="none" stroke="#dde3e6" stroke-width="4"/>
    <circle cx="80" cy="76" r="39" fill="var(--blue)"/>
    <rect x="68" y="60" width="24" height="30" rx="2" fill="none" stroke="#fff" stroke-width="2.5"/>
    <rect x="74" y="56" width="12" height="6" fill="#fff"/>
    <circle cx="80" cy="77" r="6" fill="none" stroke="#fff" stroke-width="2.5"/>
  </svg>
  <h3>Our Mission</h3>
  <p>Lorem Ipsum is simply dummy text of the printing and typesetting industry. Lorem Ipsum has been standard dummy text.</p>
  <a class="btn-outline">View More</a>
</div>
<div class="intro-card" style="left:460px">
  <svg width="160" height="140" viewBox="0 0 160 140">
    <path d="M80 14 A62 62 0 1 0 142 76" fill="none" stroke="#dde3e6" stroke-width="5"/>
    <path d="M134 70 l8 10 l8 -10" fill="none" stroke="#dde3e6" stroke-width="4"/>
    <circle cx="80" cy="76" r="39" fill="var(--blue)"/>
    <circle cx="80" cy="60" r="5" fill="#fff"/>
    <rect x="74" y="68" width="12" height="16" rx="2" fill="#fff"/>
    <rect x="75" y="82" width="4" height="14" fill="#fff"/><rect x="81" y="82" width="4" height="14" fill="#fff"/>
  </svg>
  <h3>Who We Are</h3>
  <p>Lorem Ipsum is simply dummy text of the printing and typesetting industry. Lorem Ipsum has been standard dummy text.</p>
  <a class="btn-outline">View More</a>
</div>
<div class="intro-card" style="left:760px">
  <svg width="160" height="140" viewBox="0 0 160 140">
    <path d="M80 14 A62 62 0 1 0 142 76" fill="none" stroke="#dde3e6" stroke-width="5"/>
    <path d="M134 70 l8 10 l8 -10" fill="none" stroke="#dde3e6" stroke-width="4"/>
    <circle cx="80" cy="76" r="39" fill="var(--blue)"/>
    <circle cx="80" cy="64" r="8" fill="#fff"/>
    <path d="M64 94 Q66 76 80 76 Q94 76 96 94 Z" fill="#fff"/>
  </svg>
  <h3>What We Do</h3>
  <p>Lorem Ipsum is simply dummy text of the printing and typesetting industry. Lorem Ipsum has been standard dummy text.</p>
  <a class="btn-outline">View More</a>
</div>

<section class="offer" role="img" aria-label="Dark background photo of joined hands">
  <h2 class="section-title"><span class="sq"></span>What We Offer</h2>

  <div class="offer-item" style="left:157px">
    <svg width="78" height="78" viewBox="0 0 78 78"><circle cx="39" cy="39" r="39" fill="var(--blue)"/><path d="M28 52 L36 30 L52 24 L46 40 Z" fill="#fff"/><line x1="28" y1="52" x2="39" y2="37" stroke="var(--blue)" stroke-width="2"/></svg>
    <h3>Implement</h3>
    <p>Lorem Ipsum is simply dummy text of the printing and typesetting industry. Lorem Ipsum has been standard</p>
    <a class="btn-outline">View More</a>
  </div>
  <div class="offer-item" style="left:383px">
    <svg width="78" height="78" viewBox="0 0 78 78"><circle cx="39" cy="39" r="39" fill="var(--blue)"/><rect x="23" y="24" width="32" height="22" fill="none" stroke="#fff" stroke-width="2.5"/><polyline points="28,40 35,33 41,37 49,29" fill="none" stroke="#fff" stroke-width="2"/><line x1="30" y1="46" x2="26" y2="56" stroke="#fff" stroke-width="2.5"/><line x1="48" y1="46" x2="52" y2="56" stroke="#fff" stroke-width="2.5"/></svg>
    <h3>Train</h3>
    <p>Lorem Ipsum is simply dummy text of the printing and typesetting industry. Lorem Ipsum has been standard</p>
    <a class="btn-outline">View More</a>
  </div>
  <div class="offer-item" style="left:606px">
    <svg width="78" height="78" viewBox="0 0 78 78"><circle cx="39" cy="39" r="39" fill="var(--blue)"/><rect x="35" y="18" width="7" height="22" rx="3.5" fill="#fff"/><path d="M30 36 Q30 34 33 34 L48 34 Q52 34 52 40 L52 50 Q52 58 44 58 L38 58 Q32 58 30 50 Z" fill="#fff"/></svg>
    <h3>Select</h3>
    <p>Lorem Ipsum is simply dummy text of the printing and typesetting industry. Lorem Ipsum has been standard</p>
    <a class="btn-outline">View More</a>
  </div>
  <div class="offer-item" style="left:832px">
    <svg width="78" height="78" viewBox="0 0 78 78"><circle cx="39" cy="39" r="39" fill="var(--blue)"/><polyline points="24,22 24,54 56,54" fill="none" stroke="#fff" stroke-width="2.5"/><polyline points="28,48 36,38 42,43 52,28" fill="none" stroke="#fff" stroke-width="2.5"/><path d="M47 28 L53 27 L52 33" fill="none" stroke="#fff" stroke-width="2.5"/></svg>
    <h3>Improve</h3>
    <p>Lorem Ipsum is simply dummy text of the printing and typesetting industry. Lorem Ipsum has been standard</p>
    <a class="btn-outline">View More</a>
  </div>
</section>

<section class="lower">
  <h2 class="section-title" style="left:161px"><span class="sq"></span>Client Stories</h2>
  <h2 class="section-title" style="left:460px"><span class="sq"></span>News &amp; Events</h2>
  <h2 class="section-title" style="left:755px"><span class="sq"></span>How Can We Help?</h2>

  <div class="story">
    <div class="photo lab" style="left:161px" role="img" aria-label="Photo of pharmacy staff in white coats in front of shelves"></div>
    <h4 style="left:161px;top:1776px">Health Systems</h4>
    <p style="left:161px;top:1798px">Lorem Ipsum is simply dummy text of the printing and typesetting industry. Lorem Ipsum has been standard dummy text.</p>
  </div>

  <div class="news">
    <div class="photo hands" style="left:460px" role="img" aria-label="Photo of a caregiver holding a patient's hands"></div>
    <span class="date" style="left:460px;top:1778px">May 02, 2014</span>
    <h4 style="left:460px;top:1797px">Hardwire High Reliablity Maximize ...</h4>
    <p style="left:460px;top:1820px">Lorem Ipsum is simply dummy text of the printing and typesetting industry. Lorem Ipsum has... <span class="more">[...]</span></p>
  </div>

  <form>
    <div class="field" style="top:1610px;height:33px">Your Name</div>
    <div class="field" style="top:1658px;height:33px">Your Email</div>
    <div class="field" style="top:1708px;height:98px">Questions/Comments</div>
    <a class="btn-dark">SUBMIT</a>
  </form>
</section>

<footer class="site-footer">
  <div class="brand"><span class="brand-mark"></span>CrestVane</div>
  <div class="f-address">
    97 Lorem Ipsum, Street 400,<br>Site amet text, Zip 01234<br>
    <div style="margin-top:8px"><b>P :</b> 555.014.2297</div>
    <div style="margin-top:2px"><b>E :</b> <span class="link">support@crestvanesolutions.example</span><br>&nbsp;&nbsp;&nbsp;&nbsp;<span class="link">info@crestvanesolutions.example</span></div>
  </div>

  <h5 style="left:423px">Solution</h5>
  <ul class="f-links">
    <li>Advisory Services</li><li>Information Technology</li><li>Healthcare Reform</li><li>Innovative Solutions</li><li>Patient Safety</li>
  </ul>

  <h5 style="left:612px">Newsletter Sign Up</h5>
  <div class="f-input" style="top:78px">Name</div>
  <div class="f-input" style="top:115px">Email_address</div>
  <a class="f-btn">SUBSCRIBE NOW!</a>

  <h5 style="left:920px">Connect With Us</h5>
  <div class="social"><span></span><span></span><span></span><span></span></div>
</footer>

<div class="bottom-bar">
  <span class="copy">© 2014 - CrestVane Solutions LLC. All Rights Reserved.</span>
  <span class="legal">Home | About | Services | Solutions | Contact | Terms of Use | Privacy</span>
</div>

</body>
</html>
```